HiItsJonBrell.com needs a modern, eye-catching business card design

My name is Jon Brell and I own a video training (software development industry) website. I need a business card design that is eye catching for when I travel to conferences or do seminars. I would prefer something simple but bold. Something along the lines of this: https://pixvaultstatic.example/gallery_img/530172/44018/44018_9917302_530172_image.jpg

Note that I do not have a specific logo, but I do have an caricature I use on my site of myself. I've not attached it because I'm not really a fan of having it on my business cards. I would prefer lettering instead of an image. You can go to my website (https://hiitsjonbrell.com) for inspiration.

I want to add the following information on my card (the order of these, their size, and their casing is up to you):

Jon Brell
jon@HiItsJonBrell.com
@HiItsJonBrell
HiItsJonBrell.com
vidsharehub.example/HiItsJonBrell

I would also like to have somewhere on the card a small ad that says "Get a free course at https://HiItsJonBrell.com/FreeCourse". Feel free to play with that wording or layout if you need. I would prefer this text to be at the bottom of the card and subtle. Some small eye-catching thing might be ok but nothing huge or garish.

I plan on printing this card at pressquill.example (https://www.pressquill.example/us/design-guidelines/business-cards.html). I would like it to be the standard size (3.66" x 2.16"). I would prefer rounded corners and horizontal orientation. This is a two-side design. I would prefer the side with all of the information be primarily white but I like color text (again, flexible on that). On the front side, I like simple. Maybe just HiItsJonBrell.com (casing on that is up to you - whatever looks and reads the best - that goes for all of the casing). As for font choices, I prefer a modern, clean font. For example, Open Sans Light can be a nice option.

Website Info (might be helpful for the card):
Color Palette

Darkest blue - #263246
Alternate blue - #2F4E6A
Light blue - #2A98C3
Orange - #FF6201
White - #FFFFFF

Font for Jon Brell Logo

Jellyka Estryas Handwriting
http://www.typecrate.example/jellyka_estryas_handwriting.font

Fonts for Site Content and VidShare Thumbnails

Lovelo (bold title font)
http://www.glyphmill.example/lovelo-font/

Open Sans (body font)
http://www.letterbarn.example/fonts/open-sans

Industry/Entity Type

Software Development

Contact Information for Business Card

Jon Brell
jon@HiItsJonBrell.com
@HiItsJonBrell
HiItsJonBrell.com
vidsharehub.example/HiItsJonBrell

Get a free course at https://HiItsJonBrell.com/FreeCourse

Colors

Designer to choose colors to be used in the design.

Requirements
Nice to have
• Modern color - maybe primarily a color on the front and then that color as an accent on the back.
Should not have
• Lots of colors - I LOVE color but do not want a rainbow of colors on the card.

```html
<!DOCTYPE html>
<html lang="en">
<head>
<meta charset="utf-8">
<title>Jon Brell — Business Card</title>
<link rel="stylesheet" href="https://fonts.googleapis.com/css2?family=Lato:wght@300;400&display=swap">
<style>
  :root {
    --navy: #22324a;
    --white: #ffffff;
    --backdrop: #e9e6e1;
    --text-light: #dfe5ee;
  }
  * { box-sizing: border-box; margin: 0; padding: 0; }
  html, body {
    width: 1200px;
    height: 900px;
    overflow: hidden;
    background: var(--backdrop);
    font-family: "Lato", Arial, sans-serif;
  }
  .canvas {
    width: 1200px;
    height: 900px;
    display: flex;
    flex-direction: column;
    align-items: center;
    justify-content: center;
    gap: 48px;
  }
  .card {
    position: relative;
    width: 640px;
    height: 378px;
    border-radius: 6px;
    overflow: hidden;
    box-shadow: 0 6px 18px rgba(0, 0, 0, 0.18);
  }
  .card--front { background: var(--navy); }
  .card--back { background: var(--white); }

  .wordmark {
    font-family: "Lato", Arial, sans-serif;
    font-weight: 300;
    letter-spacing: 1px;
  }
  .card--front .wordmark {
    position: absolute;
    left: 0; right: 0;
    top: 128px;
    text-align: center;
    font-size: 70px;
    color: var(--white);
  }
  .card--back .wordmark {
    position: absolute;
    right: 44px;
    top: 44px;
    font-size: 50px;
    color: var(--navy);
  }

  .contact-list {
    position: absolute;
    left: 40px;
    top: 150px;
    list-style: none;
    color: var(--navy);
    font-size: 17px;
    line-height: 24px;
  }
  .contact-list li { display: flex; align-items: center; gap: 8px; }
  .contact-icon { width: 13px; height: 13px; flex: none; fill: var(--navy); }

  .promo-band {
    position: absolute;
    left: 0; right: 0; bottom: 0;
    height: 130px;
    background: var(--navy);
    color: var(--text-light);
    text-align: right;
    padding: 26px 44px 0 0;
  }
  .promo-lead { font-size: 16px; padding-right: 60px; }
  .promo-url { font-size: 22px; margin-top: 6px; }
</style>
</head>
<body>
<main class="canvas">
  <section class="card card--front" aria-label="Card front">
    <div class="wordmark">Jon Brell</div>
  </section>

  <section class="card card--back" aria-label="Card back">
    <div class="wordmark">Jon Brell</div>
    <ul class="contact-list">
      <li>
        <svg class="contact-icon" viewBox="0 0 13 13" aria-hidden="true"><rect x="0" y="2" width="13" height="9"/><path d="M0 2 L6.5 7 L13 2" fill="none" stroke="#fff" stroke-width="1.2"/></svg>
        jon@HiItsJonBrell.com
      </li>
      <li>
        <svg class="contact-icon" viewBox="0 0 13 13" aria-hidden="true"><circle cx="6.5" cy="6.5" r="6"/><path d="M1 6.5 H12 M6.5 1 C3.5 4 3.5 9 6.5 12 M6.5 1 C9.5 4 9.5 9 6.5 12" fill="none" stroke="#fff" stroke-width="0.9"/></svg>
        www.HiItsJonBrell.com
      </li>
      <li>
        <svg class="contact-icon" viewBox="0 0 13 13" aria-hidden="true"><circle cx="6.5" cy="6.5" r="5.5"/></svg>
        chirper@HiItsJonBrell
      </li>
      <li>
        <svg class="contact-icon" viewBox="0 0 13 13" aria-hidden="true"><rect x="1" y="1" width="11" height="11"/></svg>
        vidsharehub.example/HiItsJonBrell
      </li>
    </ul>
    <div class="promo-band">
      <p class="promo-lead">Get a free course&nbsp; at</p>
      <p class="promo-url">https://HiItsJonBrell.com/FreeCourse</p>
    </div>
  </section>
</main>
</body>
</html>
```